Luxury Brand Real Estate For Sale sign

**Update** I've added some examples from the internet of other signs that have a look similar to what I would like to see. I do not want my personal name in the sign. And the word FOR SALE Does not need to be so large - it can be more subtle.
I want to create a Real Estate for sale sign for my company that will be used for luxury/higher end real estate listings. I’m sharing my business card as well as a logo with new teal color to show what we're moving towards: we’re using Teal, white, black and gold.
Hoping the sign is simple, sophisticated and eye catching.
The sign should be 24" wide by 30" tall including the company name: Harbor Crest Realty Group and our logo, office phone number 727-555-0148 and website www.hcrgproperty.example the words "For Sale"
Optional to add this e-mail address info@hcrgproperty.example to the sign
Luxury home buyers
Real Estate

```html
<!DOCTYPE html>
<html lang="en">
<head>
<meta charset="utf-8">
<title>Harbor Crest Realty Group – For Sale Sign</title>
<link href="https://fonts.googleapis.com/css2?family=Josefin+Sans:wght@400;600;700&display=swap" rel="stylesheet">
<style>
  :root {
    --backdrop: #2b2b2d;
    --sign-dark: #0c0d10;
    --sign-mid: #1d1e22;
    --brand-blue: #48bfec;
    --wave-blue: #5fc3e8;
    --paper: #ffffff;
    --ink: #0b0b0c;
  }
  html, body {
    margin: 0;
    width: 1200px;
    height: 1187px;
    overflow: hidden;
    background: var(--backdrop);
    font-family: "Josefin Sans", "Futura", sans-serif;
  }
  h1, h2, p { margin: 0; }
  .sign {
    position: absolute;
    left: 222px;
    top: 122px;
    width: 739px;
    height: 924px;
    overflow: hidden;
    background: radial-gradient(circle at 50% 45%, var(--sign-mid) 0%, var(--sign-mid) 35%, var(--sign-dark) 80%);
  }
  .sign__wave {
    position: absolute;
    inset: 0;
  }
  .brand {
    position: absolute;
    top: 92px;
    left: 0;
    width: 100%;
    display: flex;
    justify-content: center;
    align-items: center;
    gap: 16px;
  }
  .brand__mark {
    width: 34px;
    height: 34px;
    border: 4px solid var(--brand-blue);
    box-sizing: border-box;
  }
  .brand__name {
    color: var(--brand-blue);
    font-weight: 600;
    font-size: 31px;
    letter-spacing: 0.5px;
    line-height: 1;
    padding-top: 6px;
  }
  .headline {
    position: absolute;
    left: 0;
    width: 100%;
    text-align: center;
    font-weight: 700;
    line-height: 1;
  }
  .headline--for {
    top: 212px;
    left: -8px;
    color: var(--brand-blue);
    font-size: 198px;
    letter-spacing: 4px;
  }
  .headline--sale {
    top: 392px;
    color: var(--paper);
    font-size: 204px;
    letter-spacing: 2px;
  }
  .rule {
    position: absolute;
    top: 583px;
    left: 127px;
    width: 487px;
    height: 2px;
    background: linear-gradient(90deg, transparent, var(--brand-blue) 12%, var(--brand-blue) 88%, transparent);
  }
  .phone {
    position: absolute;
    top: 624px;
    left: 0;
    width: 100%;
    text-align: center;
    color: var(--paper);
    font-weight: 700;
    font-size: 79px;
    letter-spacing: 0;
    line-height: 1;
  }
  .website {
    position: absolute;
    top: 822px;
    left: 0;
    width: 100%;
    text-align: center;
    color: var(--ink);
    font-size: 38px;
    font-weight: 700;
    line-height: 1;
  }
  .website__prefix {
    font-weight: 600;
  }
</style>
</head>
<body>
  <main class="sign">
    <svg class="sign__wave" viewBox="0 0 739 924" width="739" height="924" aria-hidden="true">
      <path d="M0 748 C120 790 260 780 420 755 C560 733 660 725 739 760 L739 924 L0 924 Z" fill="var(--wave-blue)"/>
      <path d="M0 751 C110 800 250 802 420 778 C560 757 660 745 739 763 L739 924 L0 924 Z" fill="var(--paper)"/>
    </svg>

    <header class="brand">
      <span class="brand__mark"></span>
      <span class="brand__name">Harbor Crest Realty Group</span>
    </header>

    <h1 class="headline headline--for">FOR</h1>
    <h2 class="headline headline--sale">SALE</h2>

    <div class="rule"></div>

    <p class="phone">727-555-0148</p>

    <p class="website"><span class="website__prefix">www.</span>hcrgproperty.example</p>
  </main>
</body>
</html>
```